Fishing Tackle Product Packaging Backdrop/Template

Hi Designers,
we require a versatile packaging backdrop/template design for our fishing tackle brand. The design will be used in printed packaging for a range of products from small to large so would need to be scaleable. It will most commonly be used on small printed card tags (2x3"), but we would like to be able to use it for other packaging aswell.
A section for our product details, which we can edit ourselves would be essential, this way we can use the template for any of our products. The back of the card will need a space for our barcodes.
The design needs to be predominantly macsuline and appeal to the modern carp angler. It also needs to pop so that our goods really stand out against our competitors. Please see our logo attached. It'd also be great to see our web address at the bottom, on both sides of the design: www.brelvanrigs.co.uk

Thanks in advance and good luck!
Brelvan Rigs Team
Updates

Target Market(s)

Male Carp Anglers (aprox ages 18-60)

Industry/Entity Type

Fishing Tackle

Requirements
Must have
• Our logo and web address, with a section for a barcode and product title/info

```html
<!DOCTYPE html>
<html lang="en">
<head>
<meta charset="utf-8">
<title>Brelvan Rigs – Product Tag Template</title>
<link href="https://fonts.googleapis.com/css2?family=Roboto:wght@400;700;900&family=Roboto+Condensed:wght@700&display=swap" rel="stylesheet">
<style>
  :root {
    --bg-light: #666666;
    --bg-dark: #2f2f2f;
    --green-top: #3d5a06;
    --green-mid: #2b4204;
    --green-bottom: #1a2903;
    --green-art: #35500a;
    --green-bullet: #4f7a12;
    --ink-dark: #1f3004;
    --white: #ffffff;
    --bronze-dark: #6e5532;
    --bronze: #a88c68;
    --silver: #e8e4d8;
  }
  * { margin: 0; padding: 0; box-sizing: border-box; }
  html, body { width: 1200px; height: 1000px; overflow: hidden; }
  body {
    background: radial-gradient(circle at 50% 50%, var(--bg-light), var(--bg-dark) 75%);
    font-family: 'Roboto', Arial, sans-serif;
    color: var(--white);
    position: relative;
  }
  .tag {
    position: absolute;
    top: 139px;
    width: 483px;
    height: 723px;
    border-radius: 24px;
    overflow: hidden;
    background: linear-gradient(to bottom, var(--green-top) 0%, var(--green-mid) 45%, var(--green-bottom) 100%);
  }
  .tag--front { left: 85px; }
  .tag--back { left: 632px; }

  /* Front */
  .brand-mark {
    position: absolute;
    top: 60px; left: 0; width: 100%;
    display: flex; align-items: center; justify-content: center; gap: 10px;
  }
  .brand-mark__dot {
    width: 22px; height: 22px; border-radius: 50%;
    background: var(--silver);
  }
  .brand-mark__name {
    font-family: 'Roboto', Arial, sans-serif;
    font-weight: 900; font-size: 30px; color: var(--silver);
  }
  .product-name {
    position: absolute; top: 172px; left: 88px;
    font-weight: 900; font-size: 37px; letter-spacing: 0.3px; line-height: 1;
  }
  .feature-line {
    position: absolute; top: 356px; left: 88px;
    font-size: 21px; font-weight: 400; line-height: 1;
    margin-top: -139px;
  }
  .feature-line__rule {
    position: absolute; top: 236px; left: 247px;
    width: 148px; height: 2px; background: var(--white);
  }
  .hero-art {
    position: absolute; left: 104px; top: 290px;
    width: 273px; height: 303px;
    border-radius: 50%;
    background: radial-gradient(ellipse at center, var(--green-art) 0%, rgba(53,80,10,0.5) 55%, rgba(53,80,10,0) 72%);
  }
  .tagline-band {
    position: absolute; left: 0; bottom: 0; width: 100%; height: 65px;
    background: linear-gradient(to right, var(--bronze) 0%, var(--silver) 45%, var(--bronze) 80%, var(--bronze-dark) 100%);
    display: flex; align-items: center; justify-content: center;
  }
  .tagline {
    font-family: 'Roboto Condensed', 'Arial Narrow', sans-serif;
    font-weight: 700; font-size: 40px; color: var(--ink-dark);
  }

  /* Back */
  .back-title {
    position: absolute; top: 18px; left: 0; width: 100%;
    text-align: center;
    font-family: 'Roboto Condensed', 'Arial Narrow', sans-serif;
    font-weight: 700; font-size: 44px; line-height: 52px;
  }
  .divider {
    position: absolute; left: 0; width: 100%; height: 5px;
    background: linear-gradient(to right, var(--bronze-dark), var(--bronze) 20%, var(--silver) 50%, var(--bronze) 80%, var(--bronze-dark));
  }
  .divider--1 { top: 89px; }
  .divider--2 { top: 234px; }
  .divider--3 { top: 380px; }
  .angler-art {
    position: absolute; left: 291px; top: 101px;
    width: 192px; height: 456px;
    background: linear-gradient(to bottom, rgba(27,42,3,0.55), rgba(27,42,3,0.25) 70%, rgba(27,42,3,0));
    border-radius: 90px 0 0 40px;
  }
  .info-block { position: absolute; left: 48px; width: 400px; }
  .info-block__heading {
    font-weight: 900; font-size: 16.5px; line-height: 20px; letter-spacing: 0.2px;
  }
  .description { top: 116px; }
  .description p { font-size: 16.5px; line-height: 26px; }
  .features { top: 254px; }
  .feature-list { list-style: none; }
  .feature-list li {
    position: relative; padding-left: 25px;
    font-size: 16.5px; line-height: 20.5px;
  }
  .feature-list li::before {
    content: ""; position: absolute; left: 1px; top: 5px;
    width: 10px; height: 10px; border-radius: 50%;
    background: var(--green-bullet);
  }
  .specs { top: 402px; }
  .spec-row {
    display: flex; align-items: flex-end;
    font-size: 16.5px; line-height: 20.5px;
  }
  .spec-row__label { width: 80px; }
  .spec-row__colon { width: 12px; }
  .spec-row__fill {
    flex: 0 0 296px; height: 1px; margin-bottom: 4px;
    background: var(--white);
  }
  .barcode-space {
    position: absolute; left: 136px; top: 575px;
    width: 212px; height: 88px;
    border: 3px solid var(--white);
    padding: 3px;
  }
  .barcode-space__inner {
    width: 100%; height: 100%;
    background: var(--white);
    border: 2px solid var(--green-bottom);
  }
  .web-address {
    position: absolute; top: 678px; left: 0; width: 100%;
    text-align: center; font-size: 20px; line-height: 26px;
  }
</style>
</head>
<body>

<section class="tag tag--front">
  <div class="brand-mark">
    <span class="brand-mark__dot"></span>
    <span class="brand-mark__name">Brelvan Rigs</span>
  </div>
  <h1 class="product-name">PRODUCT NAME</h1>
  <p class="feature-line" style="top:356px;">FEATURE LINE</p>
  <span class="feature-line__rule"></span>
  <div class="hero-art" role="img" aria-label="Faint illustration of a leaping carp"></div>
  <div class="tagline-band">
    <p class="tagline">Gear Up. Catch More.</p>
  </div>
</section>

<section class="tag tag--back">
  <h2 class="back-title">BRELVAN RIGS</h2>
  <span class="divider divider--1"></span>
  <div class="angler-art" role="img" aria-label="Faint silhouette of an angler holding a fishing rod"></div>

  <div class="info-block description">
    <h3 class="info-block__heading">PRODUCT DESCRIPTION</h3>
    <p>Lorem ipsum dolor sit amet consectetur adipiscing elit. Dolor sit amet consectetur adipiscing elit quisque faucibus.</p>
  </div>
  <span class="divider divider--2"></span>

  <div class="info-block features">
    <h3 class="info-block__heading">KEY FEATURES</h3>
    <ul class="feature-list">
      <li>FEATURE 1</li>
      <li>FEATURE 2</li>
      <li>FEATURE 3</li>
      <li>FEATURE 4</li>
    </ul>
  </div>
  <span class="divider divider--3"></span>

  <div class="info-block specs">
    <h3 class="info-block__heading">SPECIFICATION</h3>
    <div class="spec-row"><span class="spec-row__label">Weight</span><span class="spec-row__colon">:</span><span class="spec-row__fill"></span></div>
    <div class="spec-row"><span class="spec-row__label">Lengh</span><span class="spec-row__colon">:</span><span class="spec-row__fill"></span></div>
    <div class="spec-row"><span class="spec-row__label">material</span><span class="spec-row__colon">:</span><span class="spec-row__fill"></span></div>
    <div class="spec-row"><span class="spec-row__label">Hook Size</span><span class="spec-row__colon">:</span><span class="spec-row__fill"></span></div>
  </div>

  <div class="barcode-space"><div class="barcode-space__inner"></div></div>
  <p class="web-address">brelvanrigs.co.uk</p>
</section>

</body>
</html>
```